Business Card Design

We sell Poultry & Fertilised Eggs
Black Copper Maran
French Wheaten Maran
Cayuga Ducks
Araucana
Welsummer
Show Quality Purebred Stock
Some ideas -
Gold egg on the front of the card & only the phone number on the back written like - 04 283 579 30

```html
<!DOCTYPE html>
<html lang="en">
<head>
<meta charset="utf-8">
<title>Amber Hen Poultry – Business Card</title>
<link href="https://fonts.googleapis.com/css2?family=Anton&family=Roboto+Condensed:wght@400;700&display=swap" rel="stylesheet">
<style>
  :root {
    --stage: #ece8e1;
    --card: #ffffff;
    --ink: #111111;
    --gold-band: #b8921c;
    --gold-light: #f6e27a;
    --gold-mid: #d6a92a;
    --gold-deep: #8a6410;
    --phone-fill: #f2e21a;
    --phone-edge: #3a3220;
    --soft-text: #ecd68a;
  }
  * { box-sizing: border-box; margin: 0; padding: 0; }
  html, body { width: 1200px; height: 1000px; overflow: hidden; }
  body {
    background: var(--stage);
    position: relative;
    font-family: "Roboto Condensed", sans-serif;
  }
  .card {
    position: absolute;
    width: 700px;
    height: 400px;
    left: 250px;
    background: var(--card);
    overflow: hidden;
    box-shadow: 0 6px 18px rgba(0,0,0,0.18);
  }
  .card--front { top: 60px; }
  .card--back { top: 540px; }

  /* Front */
  .brand {
    position: absolute;
    left: 28px;
    top: 0;
    height: 400px;
    display: flex;
    align-items: center;
    justify-content: center;
    gap: 12px;
    writing-mode: vertical-rl;
    transform: rotate(180deg);
  }
  .brand__dot {
    width: 18px; height: 18px;
    border-radius: 50%;
    background: var(--gold-mid);
  }
  .brand__name {
    font-family: "Anton", sans-serif;
    font-size: 34px;
    line-height: 1;
    letter-spacing: 1px;
    color: var(--ink);
    text-transform: uppercase;
    white-space: nowrap;
  }
  .nest-photo {
    position: absolute;
    left: 110px;
    top: 0;
    width: 590px;
    height: 400px;
    background:
      radial-gradient(ellipse 35% 30% at 50% 45%, var(--gold-light) 0%, var(--gold-mid) 55%, transparent 75%),
      linear-gradient(160deg, #fff8dc 0%, var(--gold-mid) 45%, var(--gold-deep) 100%);
  }

  /* Back */
  .band {
    position: absolute;
    width: 1000px;
    height: 200px;
    left: -150px;
    top: 100px;
    background: var(--gold-band);
    transform: rotate(20deg);
    display: flex;
    flex-direction: column;
    justify-content: center;
    padding-left: 250px;
  }
  .band__email {
    font-size: 16px;
    line-height: 20px;
    font-weight: 700;
    color: #ffffff;
    letter-spacing: 0.3px;
  }
  .band__phone {
    font-family: "Anton", sans-serif;
    font-size: 64px;
    line-height: 72px;
    color: var(--phone-fill);
    -webkit-text-stroke: 2px var(--phone-edge);
    letter-spacing: 2px;
  }
  .band__stock {
    font-size: 11px;
    line-height: 13px;
    color: var(--soft-text);
    margin-top: 4px;
  }
</style>
</head>
<body>
  <section class="card card--front">
    <div class="brand">
      <span class="brand__dot"></span>
      <span class="brand__name">Amber Hen Poultry</span>
    </div>
    <div class="nest-photo" role="img" aria-label="Photograph of three golden eggs resting in a straw nest"></div>
  </section>

  <section class="card card--back">
    <div class="band">
      <p class="band__email">amberhenpoultry@example.com</p>
      <p class="band__phone">04 283 579 30</p>
      <div class="band__stock">
        <p>Black Copper Maran</p>
        <p>French Wheaten Maran</p>
        <p>Cayuga Ducks</p>
        <p>Araucana</p>
        <p>Welsummer</p>
      </div>
    </div>
  </section>
</body>
</html>
```